Website for Life Strategies business

We need a website to present our video, audio and print content to subcribers at Vivid Horizon Mentors. We will offer a team of coaches who can help people breakthrough the barriers that keep them from reaching their physical, spiritual, financial, leadership and relationship goals.

Target Market(s)

Anyone who needs help with strategies to take their life to a new level of success.

Industry/Entity Type

Life Coaching

Logo Text

Vivid Horizon Mentors

Number of Pages Required

5+ page

Colors

Designer to choose colors to be used in the design.

Requirements
Must have
• The ability to present content as a package that includes Word Documents, videos and audio content as well as to be able to display books for sale. Each week their would be a new package for subscribers to access. It should provide the ability for subscribers to comment on the material and share how their lives were changed by the content. Should also include a shop page to offer merchandise for sale.
Nice to have
• Not sure
Should not have
• Not sure

```html
<!DOCTYPE html>
<html lang="en">
<head>
<meta charset="utf-8">
<title>Vivid Horizon Mentors</title>
<link href="https://fonts.googleapis.com/css2?family=Open+Sans:ital,wght@0,400;0,600;0,700;1,400&display=swap" rel="stylesheet">
<style>
:root{
  --blue:#1aa3d9;
  --green:#7cc242;
  --dark:#222;
  --text:#444;
  --muted:#666;
  --grey-bg:#f0f0ec;
  --card-bg:#ebebeb;
  --footer:#1b1b1b;
  --line:#d6d6d6;
}
*{margin:0;padding:0;box-sizing:border-box}
html,body{width:1200px;height:3830px;overflow:hidden}
body{font-family:"Open Sans",Arial,sans-serif;color:var(--text);background:#fff;position:relative}
.abs{position:absolute}
.btn{display:inline-flex;align-items:center;justify-content:center;color:#fff;font-weight:600;font-size:15px;border-radius:2px}
.btn-green{background:var(--green)}
.btn-blue{background:var(--blue)}
.btn-dark{background:#444}

/* header */
.header{top:0;left:0;width:1200px;height:140px}
.brand{left:100px;top:22px;display:flex;align-items:center;gap:14px}
.brand-dot{width:74px;height:74px;border-radius:50%;background:var(--blue)}
.brand-name{font-size:22px;font-weight:700;color:var(--blue);line-height:1.1;width:160px}
.account{right:100px;top:46px;display:flex;gap:14px}
.account .btn{width:122px;height:44px;font-size:15px;gap:10px}

.nav{top:140px;left:0;width:1200px;height:40px;background:var(--blue);display:flex;padding:0 100px;justify-content:space-between}
.nav a{color:#fff;font-size:14px;font-weight:600;text-decoration:none;display:flex;align-items:center;justify-content:center;padding:0 20px}
.nav a.active{background:var(--green);width:105px}

/* hero */
.hero{top:180px;left:0;width:1200px;height:515px}
.hero-photo{width:100%;height:100%;background:
  radial-gradient(circle at 70% 78%, #fff6c9 0%, #f7c257 14%, #e28d2c 34%, #9a5c2c 60%, #3a2a22 100%)}
.hero-copy{left:600px;top:182px;width:520px;text-align:center}
.hero-copy h1{font-size:31px;font-weight:700;color:var(--dark);line-height:1.3}
.hero-copy .btn{margin-top:28px;width:130px;height:44px}

/* section heads */
.sec-title{font-size:31px;font-weight:700;color:var(--dark)}
.sec-title span{color:var(--blue)}
.sec-title.green span{color:var(--green)}
.divider{height:20px;display:flex;align-items:center;gap:0}
.divider i{flex:1;height:1px;background:var(--line)}
.divider b{width:18px;height:18px;border-radius:50%;background:#cfcfcf;margin:0 8px}
.center{text-align:center}
.lead{font-size:13px;line-height:1.7;color:var(--muted)}

/* about */
.about{top:695px;left:0;width:1200px;height:352px}
.about-photo{left:100px;top:43px;width:362px;height:260px;background:linear-gradient(135deg,#e7e2dc,#c9c3bc 55%,#5a8db5)}
.about-body{left:487px;top:50px;width:613px}
.about-body .divider{margin:10px 0 20px}
.about-body p{font-size:13px;line-height:1.85;color:var(--muted)}
.about-body .btn{margin-top:26px;width:112px;height:42px}

/* help */
.help{top:1047px;left:0;width:1200px;height:473px;background:var(--grey-bg)}
.help .sec-title{position:absolute;top:44px;width:100%}
.help .divider{position:absolute;top:100px;left:330px;width:540px}
.help .lead{position:absolute;top:130px;left:110px;width:980px}
.help-item{top:212px;width:220px;text-align:center}
.help-ring{width:128px;height:128px;margin:0 auto;border-radius:50%;border:5px solid var(--green);border-top-color:transparent;border-right-color:#e1e1dc;display:flex;align-items:center;justify-content:center}
.help-icon{width:92px;height:92px;border-radius:50%;border:2px solid #bbb;background:#fff;display:flex;align-items:center;justify-content:center}
.help-item h3{font-size:17px;font-weight:600;color:var(--dark);margin-top:16px}
.help-item p{font-size:12px;line-height:1.5;color:var(--muted);margin-top:4px}
.help-item p em{color:var(--green);font-style:normal}
.arrow{font-size:34px;color:#999;top:0}

/* services */
.services{top:1520px;left:0;width:1200px;height:670px}
.services .sec-title{position:absolute;top:36px;width:100%}
.services .divider{position:absolute;top:92px;left:330px;width:540px}
.services .lead{position:absolute;top:122px;left:160px;width:880px}
.svc-brand{left:110px;top:300px;width:280px;text-align:center}
.svc-brand .brand-dot{width:160px;height:160px;margin:0 auto 18px}
.svc-brand .brand-name{width:auto;font-size:25px;color:var(--blue)}
.svc-rule{left:395px;top:250px;width:1px;height:340px;background:var(--line)}
.svc-list{left:444px;top:262px;width:650px}
.svc{border-left:3px solid var(--green);padding-left:4px;margin-bottom:25px}
.svc h3{font-size:15px;font-weight:600;color:var(--dark)}
.svc p{font-size:12.5px;line-height:1.6;color:var(--muted);margin-top:4px}

/* packages */
.packages{top:2190px;left:0;width:1200px;height:447px}
.pack-photo{left:0;top:0;width:600px;height:447px;background:linear-gradient(135deg,#c6e29a,#8cc550 50%,#6aac3a)}
.pack-copy{left:0;top:95px;width:600px;text-align:center;color:#fff}
.pack-copy h2{font-size:31px;font-weight:600;margin-top:26px}
.pack-copy p{font-size:19px;margin-top:4px}
.pack-copy .btn{margin-top:26px;width:124px;height:42px}
.video-photo{left:600px;top:0;width:600px;height:447px;background:linear-gradient(120deg,#3e4a55,#8a9aa8 50%,#d6d9db)}
.play{left:860px;top:183px;width:80px;height:80px;border-radius:50%;background:rgba(0,0,0,.55);display:flex;align-items:center;justify-content:center}

/* books */
.books{top:2637px;left:0;width:1200px;height:413px}
.books .sec-title{position:absolute;top:44px;width:100%}
.books .divider{position:absolute;top:100px;left:330px;width:540px}
.book-cover{left:150px;top:160px;width:120px;height:198px;background:linear-gradient(90deg,#137fb0,#2cb3e6 18%,#29a7d9)}
.book-copy{left:325px;top:170px;width:800px}
.book-copy h3{font-size:17px;font-weight:600;color:var(--dark)}
.book-copy p{font-size:13px;line-height:1.7;color:var(--muted);margin-top:26px}
.book-copy .btn{margin-top:18px;width:120px;height:42px}

/* blog + testimonials */
.voices{top:3050px;left:0;width:1200px;height:392px;background:var(--card-bg)}
.card{top:45px;width:487px;height:290px;background:#fff;padding:26px 20px}
.card .divider{margin:10px 0 16px}
.post{display:flex;gap:10px;margin-bottom:22px}
.date{width:40px;height:44px;background:var(--green);color:#fff;text-align:center;font-size:15px;font-weight:700;line-height:1.15;padding-top:4px;flex:none}
.date small{display:block;font-size:10px;font-weight:600}
.post h4{font-size:14px;font-weight:700;color:var(--dark)}
.post p{font-size:12px;line-height:1.5;color:var(--muted)}
.quote{display:flex;gap:22px;align-items:flex-start;margin-top:6px}
.avatar{width:90px;height:90px;border-radius:50%;background:linear-gradient(135deg,#d7dde2,#9aa8b3);border:4px solid #eee;flex:none;margin-top:10px}
.quote p{font-size:12.5px;font-style:italic;line-height:1.7;color:var(--muted)}
.quote p b{color:#bbb;font-size:26px;font-style:normal;line-height:0}

/* footer */
.footer{top:3442px;left:0;width:1200px;height:344px;background:var(--footer);color:#ddd}
.footer h3{font-size:18px;font-weight:600;color:#fff;margin-bottom:20px}
.f-col{top:50px}
.links li{list-style:none;font-size:13px;line-height:25.5px}
.links li::before{content:"›";margin-right:8px;color:#aaa}
.contact li{list-style:none;display:flex;gap:10px;font-size:13px;line-height:1.45;margin-bottom:18px;align-items:flex-start}
.contact svg{flex:none;margin-top:1px}
.field{width:238px;height:38px;background:#fff;font-size:12px;color:#555;padding:8px 10px;margin-bottom:8px}
.field.tall{height:72px}
.f-submit{width:118px;height:38px;margin-top:8px;font-size:14px}
.f-brand{left:880px;top:60px;width:220px;text-align:center}
.f-brand .brand-dot{width:128px;height:128px;margin:0 auto 16px;background:#fff}
.f-brand .brand-name{width:auto;color:#fff;font-size:21px}
.copyright{top:3786px;left:0;width:1200px;height:44px;background:var(--green);color:#fff;font-size:13px;font-weight:600;display:flex;align-items:center;justify-content:center}
</style>
</head>
<body>

<header class="header abs">
  <div class="brand abs"><div class="brand-dot"></div><div class="brand-name">Vivid Horizon Mentors</div></div>
  <div class="account abs">
    <a class="btn btn-blue">
      <svg width="16" height="16" viewBox="0 0 16 16"><path d="M2 7h8M7 4l3 3-3 3" stroke="#fff" stroke-width="2" fill="none"/><path d="M10 2h4v12h-4" stroke="#fff" stroke-width="2" fill="none"/></svg>Login</a>
    <a class="btn btn-green">
      <svg width="16" height="16" viewBox="0 0 16 16"><circle cx="8" cy="5" r="3.5" fill="#fff"/><path d="M1 16c0-5 14-5 14 0z" fill="#fff"/></svg>Register</a>
  </div>
</header>

<nav class="nav abs">
  <a class="active">Home</a><a>About Us</a><a>Coaching</a><a>Services</a><a>Shop</a><a>Blog</a><a>Testimonials</a><a>Contact Us</a>
</nav>

<section class="hero abs">
  <div class="hero-photo" role="img" aria-label="Person with raised arms standing on a rocky cliff at sunset"></div>
  <div class="hero-copy abs">
    <h1>We Offer Life Coaching Business<br>To Individuals And Teams</h1>
    <a class="btn btn-green">Learn More</a>
  </div>
</section>

<section class="about abs">
  <div class="about-photo abs" role="img" aria-label="Group yoga class in a bright studio"></div>
  <div class="about-body abs">
    <h2 class="sec-title">About <span>Vivid Horizon Mentors</span></h2>
    <div class="divider"><b></b><i></i></div>
    <p>Lorem ipsum dolor sit amet, consectetuer adipiscing elit, sed diam nonummy nibh euismod tincidunt ut laoreet dolore magna aliquam erat volutpat. Ut wisi enim ad minim veniam, quis nostrud exerci tation ullamcorper suscipit lobortis nisl ut aliquip ex ea commodo consequat. Duis autem vel eum iriure dolor in hendrerit in vulputate velit esse molestie consequat, vel illum dolore eu feugiat nulla facilisis at vero eros et accumsan et iusto odio dignissim qui blandit praesent luptatum zzril</p>
    <a class="btn btn-green">Read More</a>
  </div>
</section>

<section class="help abs">
  <h2 class="sec-title center">How We <span>Help You</span></h2>
  <div class="divider"><i></i><b></b><i></i></div>
  <p class="lead center">Sed ut perspiciatis unde omnis iste natus error sit voluptatem accusantium doloremque laudantium, totam rem aperiam, eaque ipsa quae ab illo inventore veritatis et quasi architecto beatae vitae dicta sunt explicabo. Nemo enim ipsam voluptatem quia voluptas sit aspernatur aut odit aut fugit</p>

  <div class="arrow abs" style="left:56px;top:285px">‹</div>
  <div class="arrow abs" style="left:1128px;top:285px">›</div>

  <div class="help-item abs" style="left:93px">
    <div class="help-ring"><div class="help-icon"><svg width="44" height="44" viewBox="0 0 44 44"><circle cx="22" cy="9" r="6" fill="var(--green)"/><path d="M8 17l14 4 14-4M22 21v10l-8 10M22 31l8 10" stroke="var(--green)" stroke-width="4" fill="none" stroke-linecap="round"/></svg></div></div>
    <h3>Physical</h3>
    <p>Ut enim ad minim veniam, quis nostrud exercitation ullamco laboris nisi ut aliquip ex ea ...<em>[+]</em></p>
  </div>
  <div class="help-item abs" style="left:350px">
    <div class="help-ring"><div class="help-icon"><svg width="44" height="44" viewBox="0 0 44 44"><circle cx="22" cy="9" r="6" fill="#444"/><path d="M22 17v14M8 28l14-6 14 6M6 38h32" stroke="#444" stroke-width="4" fill="none" stroke-linecap="round"/></svg></div></div>
    <h3>Spiritual</h3>
    <p>Ut enim ad minim veniam, quis nostrud exercitation ullamco laboris nisi ut aliquip ex ea ...<em>[+]</em></p>
  </div>
  <div class="help-item abs" style="left:610px">
    <div class="help-ring"><div class="help-icon"><svg width="48" height="48" viewBox="0 0 48 48"><circle cx="24" cy="24" r="20" fill="none" stroke="#444" stroke-width="4"/><text x="24" y="33" text-anchor="middle" font-family="Open Sans,sans-serif" font-size="26" font-weight="700" fill="#444">$</text></svg></div></div>
    <h3>Financial</h3>
    <p>Ut enim ad minim veniam, quis nostrud exercitation ullamco laboris nisi ut aliquip ex ea ...<em>[+]</em></p>
  </div>
  <div class="help-item abs" style="left:870px">
    <div class="help-ring"><div class="help-icon"><svg width="50" height="44" viewBox="0 0 50 44"><circle cx="25" cy="10" r="6" fill="#444"/><circle cx="10" cy="16" r="5" fill="#444"/><circle cx="40" cy="16" r="5" fill="#444"/><path d="M15 40c0-16 20-16 20 0zM1 40c0-13 15-13 15-6v6zM49 40c0-13-15-13-15-6v6z" fill="#444"/></svg></div></div>
    <h3>Leadership</h3>
    <p>Ut enim ad minim veniam, quis nostrud exercitation ullamco laboris nisi ut aliquip ex ea ...<em>[+]</em></p>
  </div>
</section>

<section class="services abs">
  <h2 class="sec-title center">Our <span>Services</span></h2>
  <div class="divider"><i></i><b></b><i></i></div>
  <p class="lead center">Sed ut perspiciatis unde omnis iste natus error sit voluptatem accusantium doloremque laudantium, totam rem aperiam, eaque ipsa quae ab illo inventore veritatis et quasi architecto beatae vitae dicta sunt explicabo. Nemo enim ipsam voluptatem quia voluptas sit aspernatur aut odit aut fugit, sed quia consequuntur magni dolores eos qui ratione voluptatem sequi nesciunt. Neque porro quisquam</p>

  <div class="svc-brand abs"><div class="brand-dot"></div><div class="brand-name">Vivid Horizon Mentors</div></div>
  <div class="svc-rule abs"></div>
  <div class="svc-list abs">
    <div class="svc"><h3>Professionals ( Career Coaching )</h3><p>Lorem ipsum dolor sit amet, consectetuer adipiscing elit, sed diam nonummy nibh euismod tincidunt ut laoreet dolore magna aliquam erat volutpat.</p></div>
    <div class="svc"><h3>Individuals ( Life Coaching )</h3><p>Lorem ipsum dolor sit amet, consectetuer adipiscing elit, sed diam nonummy nibh euismod tincidunt ut laoreet dolore magna aliquam erat volutpat. Consectetuer adipiscing elit.</p></div>
    <div class="svc"><h3>Executives ( Leadership Coaching )</h3><p>Lorem ipsum dolor sit amet, consectetuer adipiscing elit, sed diam nonummy nibh euismod tincidunt ut laoreet dolore magna aliquam erat volutpat. Consectetuer adipiscing elit.</p></div>
    <div class="svc"><h3>Working Mothers ( Career, Life &amp; Work / Life Balance Coaching )</h3><p>Lorem ipsum dolor sit amet, consectetuer adipiscing elit, sed diam nonummy nibh euismod tincidunt ut laoreet dolore magna aliquam erat volutpat. Consectetuer adipiscing elit.</p></div>
  </div>
</section>

<section class="packages abs">
  <div class="pack-photo abs" role="img" aria-label="Woman working on a laptop, tinted green"></div>
  <div class="pack-copy abs">
    <svg width="80" height="80" viewBox="0 0 80 80"><path d="M20 6h30l12 12v56H20z" fill="none" stroke="#fff" stroke-width="4"/><path d="M28 44h26M28 54h26M28 64h18" stroke="#fff" stroke-width="4"/><path d="M32 18l14 8-14 8z" fill="#fff"/></svg>
    <h2>Our Packages Today</h2>
    <p>( Word Documents, Videos And Audio )</p>
    <a class="btn btn-dark">Shop Now</a>
  </div>
  <div class="video-photo abs" role="img" aria-label="Video still of a coach in conversation with a client"></div>
  <div class="play abs"><svg width="30" height="34" viewBox="0 0 30 34"><path d="M4 2l24 15L4 32z" fill="#fff"/></svg></div>
</section>

<section class="books abs">
  <h2 class="sec-title center">Check Out Our <span>Bestselling Books</span></h2>
  <div class="divider"><i></i><b></b><i></i></div>
  <div class="arrow abs" style="left:56px;top:190px">‹</div>
  <div class="arrow abs" style="left:1128px;top:190px">›</div>
  <div class="book-cover abs" role="img" aria-label="Blue book cover"></div>
  <div class="book-copy abs">
    <h3>Ut enim ad minim veniam, quis nostrud exercitation ullamco laboris nisi ut aliquip ex ea</h3>
    <p>Sed ut perspiciatis unde omnis iste natus error sit voluptatem accusantium doloremque laudantium, totam rem aperiam, eaque ipsa quae ab illo inventore veritatis et quasi architecto beatae vitae dicta sunt explicabo. Nemo enim ipsam voluptatem quia voluptas sit aspernatur aut odit aut fugit, sed quia consequuntur magni dolores eos qui ratione voluptatem sequi</p>
    <a class="btn btn-green">Shop Now</a>
  </div>
</section>

<section class="voices abs">
  <div class="card abs" style="left:100px">
    <h2 class="sec-title green">Latest <span>Blog</span></h2>
    <div class="divider"><b></b><i></i></div>
    <div class="post"><div class="date">03<small>Mar</small></div><div><h4>Lorem ipsum dolor sit amet,</h4><p>Fusce elementum, nulla vel pellentes consequat, ante nulla hendrerit arcu, ac tincidunt mauris leo.</p></div></div>
    <div class="post"><div class="date">02<small>Mar</small></div><div><h4>Lorem ipsum dolor sit amet,</h4><p>Fusce elementum, nulla vel pellentes consequat, ante nulla hendrerit arcu, ac tincidunt mauris leo.</p></div></div>
  </div>
  <div class="card abs" style="left:613px">
    <h2 class="sec-title green">What <span>People say about us?</span></h2>
    <div class="divider"><b></b><i></i></div>
    <div class="quote">
      <div class="avatar" role="img" aria-label="Client portrait"></div>
      <p><b>“</b> Mattis porttitor nulla, eget eleifend metus gravida id . Nune sollicitudin nune at tellus pretium a pulvinar purus. Mattis porttitor null, eget eleifend metus gravida id. Nune sollicitudin nune at tellus pretium a pulvinar purus.Nune sollicitudin nune at tellus.. <b>”</b></p>
    </div>
  </div>
</section>

<footer class="footer abs">
  <div class="f-col abs" style="left:100px">
    <h3>Quick Links</h3>
    <ul class="links"><li>Home</li><li>About Us</li><li>Coaching</li><li>Services</li><li>Shop</li><li>Blog</li><li>Testimonials</li><li>Contact Us</li></ul>
  </div>
  <div class="f-col abs" style="left:303px;width:250px">
    <h3>Contact Details</h3>
    <ul class="contact">
      <li><svg width="16" height="18" viewBox="0 0 16 18"><path d="M8 0a6.5 6.5 0 0 0-6.5 6.5C1.5 11 8 18 8 18s6.5-7 6.5-11.5A6.5 6.5 0 0 0 8 0z" fill="#fff"/><circle cx="8" cy="6.5" r="2.5" fill="#1b1b1b"/></svg><span>Vivid Horizon Mentors<br>8100, Lorem ipsum dolor sit amet, consectetur adipiscing elit</span></li>
      <li><svg width="16" height="16" viewBox="0 0 16 16"><circle cx="8" cy="8" r="8" fill="#fff"/><path d="M5 4l2 2-1 1.5c.6 1.3 1.4 2.1 2.5 2.5L10 9l2 2-1.3 1.3C7 12 4 9 3.7 5.3z" fill="#1b1b1b"/></svg><span>(555) 018-2740</span></li>
      <li><svg width="16" height="16" viewBox="0 0 16 16"><circle cx="8" cy="8" r="8" fill="#fff"/><path d="M5 4l2 2-1 1.5c.6 1.3 1.4 2.1 2.5 2.5L10 9l2 2-1.3 1.3C7 12 4 9 3.7 5.3z" fill="#1b1b1b"/></svg><span>(555) 018-2740</span></li>
      <li><svg width="16" height="16" viewBox="0 0 16 16"><circle cx="8" cy="8" r="8" fill="#fff"/><rect x="4" y="5" width="8" height="6" fill="none" stroke="#1b1b1b" stroke-width="1.2"/><path d="M4 5l4 3.5L12 5" fill="none" stroke="#1b1b1b" stroke-width="1.2"/></svg><span>hello@vividhorizonmentors.com</span></li>
    </ul>
  </div>
  <div class="f-col abs" style="left:597px">
    <h3>Contact Us</h3>
    <div class="field">Name</div>
    <div class="field">Email</div>
    <div class="field tall">Message</div>
    <a class="btn btn-green f-submit">Submit&nbsp;&nbsp;⟶</a>
  </div>
  <div class="f-brand abs"><div class="brand-dot"></div><div class="brand-name">Vivid Horizon Mentors</div></div>
</footer>
<div class="copyright abs">Copyright © 2017 Vivid Horizon Mentors | All Rights Reserved</div>

</body>
</html>
```